Jetzt starten So funktioniert'sAuf die Visitenkarte soll ein Logo bzw. eine Grafik dargestellt werden, welche ebenfalls auf der Website und dem Flyer genutzt werden soll wird es hier als Logo bezeichnet. Die Grafik soll ein Labyrinth und eine Person in einer scheinbar aussichtsloser Lage darstellen mit der Frage „KOMPASS gefä..
16Stein, Weg, Füße, Baby o. Kind....Sonne... Vielleicht fällt Ihnen auch etwas besseres ein. Evtl. ein Slogan wie z. B. -Kinderbetreuung mit ❤️ - Hier steht das Kind im Mittelpunkt. -Jedes Kind ist einzigartig? Oder - „Hilf mir es selbst zu tun“ aber vielleicht anders formuliert. (..
40Es müssen für zwei Geschäfte Visitenkarten, Briefpapier (A4) und Kassenkassenbelege (A6) erstellt werden. Logo und Typo im Anhang. Ein Farbkonzept besteht noch nicht. Die Idee geht in Richtung Bordeaux-Rot. Generell: (1) Sieht erstmal nach viel Beschreibung aus, bitte nicht entmutigen lass..
118Schlichtes aber direkt erkennbares Design. Koch dir Kraft , Gesundheit und Ernährungsberatung ( gut lesbar , elegant) Miriam Holtz-Ebersbach ( nicht so groß ) Grau ; Grün Töne und gerne etwas rosa Infos wie Adresse und E-Mail vielleicht in jeweilige Blöcke am unteren Rand
30Wir benötigen, passend zu unserem neuen Logo, Geschäftspapier, Visitenkarten und eine Vorlage für eine PowerPoint Präsentation (Hintergrunds-Seite)

```html
<!DOCTYPE html>
<html lang="de">
<head>
<meta charset="utf-8">
<title>Lena Marwitz – Geschäftsausstattung</title>
<link href="https://fonts.googleapis.com/css2?family=Noto+Sans:wght@400;700&display=swap" rel="stylesheet">
<style>
:root{
  --blue:#00a0e3;
  --black:#000000;
  --light-blue:#b7e3f8;
  --grey:#d2d2d2;
  --paper:#ffffff;
  --stage:#f2f2f2;
  --ink:#111111;
}
*{box-sizing:border-box;margin:0;padding:0}
html,body{width:1200px;height:900px;overflow:hidden}
body{position:relative;background:var(--stage);font-family:"Noto Sans",sans-serif;color:var(--ink)}

/* Briefbogen */
.letterhead{position:absolute;left:32px;top:19px;width:474px;height:609px;background:var(--paper);overflow:hidden;box-shadow:0 1px 4px rgba(0,0,0,.15)}
.letterhead .brand{position:absolute;right:14px;top:10px;font-size:15px;color:var(--blue)}
.letterhead .services-line{position:absolute;right:14px;top:88px;font-size:9.5px;color:var(--blue)}
.letterhead .sender-line{position:absolute;left:26px;top:106px;font-size:7px}
.letterhead .sender{position:absolute;right:14px;top:102px;text-align:right;font-size:8.5px;line-height:1.25}
.letterhead .sender .services{font-size:7.5px}
.letterhead .contact{position:absolute;right:14px;top:160px;text-align:right;font-size:9.5px;line-height:1.3}
.letterhead .deco{position:absolute;left:-60px;top:392px}
.letterhead .legal{position:absolute;right:14px;bottom:40px;text-align:right;font-size:6.5px;line-height:1.45;color:var(--blue);font-weight:700}

/* Visitenkarte klein auf dem Briefbogen */
.card-small{position:absolute;left:428px;top:421px;width:220px;height:112px;background:var(--paper);overflow:hidden;box-shadow:0 1px 5px rgba(0,0,0,.25)}
.card-small .brand{position:absolute;right:8px;top:6px;font-size:9px;color:var(--blue)}
.card-small .services{position:absolute;right:8px;top:20px;text-align:right;font-size:6px;line-height:1.2;color:var(--blue)}
.card-small .name{position:absolute;left:32px;top:42px;font-size:12px}
.card-small .contact{position:absolute;left:32px;top:60px;font-size:8.5px;line-height:1.25}
.card-small .deco{position:absolute;left:-22px;top:50px}

/* Logo und Absenderblock rechts */
.brand-block{position:absolute;right:38px;top:19px;width:500px;text-align:right}
.brand-block .brand{font-size:48px;color:var(--blue);line-height:1;margin-top:92px}
.brand-block .services-line{margin-top:46px;font-size:19px;color:var(--blue);letter-spacing:.5px}
.brand-block .sender{margin-top:10px;font-size:18px;line-height:1.3}
.brand-block .sender .services{font-size:16px}
.brand-block .contact{margin-top:28px;font-size:21px;line-height:1.3}

/* Visitenkarte groß */
.card-large{position:absolute;left:703px;top:606px;width:478px;height:270px;background:var(--paper);overflow:hidden;box-shadow:0 1px 6px rgba(0,0,0,.25)}
.card-large .brand{position:absolute;right:14px;top:12px;font-size:20px;color:var(--blue)}
.card-large .services{position:absolute;right:14px;top:68px;text-align:right;font-size:15px;line-height:1.2;color:var(--blue)}
.card-large .deco{position:absolute;left:-30px;top:140px}
.card-large .name{position:absolute;left:80px;top:105px;font-size:30px}
.card-large .contact{position:absolute;left:80px;top:152px;font-size:24px;line-height:1.25}

/* Farbpalette */
.palette-label{position:absolute;left:26px;top:796px;font-size:19px}
.palette{position:absolute;left:26px;top:836px;display:flex;gap:10px}
.swatch{width:38px;height:38px}
.swatch.black{background:var(--black)}
.swatch.blue{background:var(--blue)}
.swatch.light-blue{background:var(--light-blue)}
</style>
</head>
<body>

<section class="letterhead" aria-label="Briefbogen">
  <div class="brand">Lena Marwitz</div>
  <div class="services-line">Korrektorat • Textredaktion • Ghostwriting</div>
  <div class="sender-line">Lena Marwitz, Lindenhofweg 7, 24103 Kiel</div>
  <div class="sender">Lena <b>Marwitz</b><div class="services">Korrektorat<br>Textredaktion<br>Ghostwriting</div></div>
  <div class="contact">Lindenhofweg 7<br>24103 Kiel<br>Tel. (0 431) 7 62 40 18<br>l.marwitz@post-beispiel.de</div>
  <svg class="deco" width="300" height="240" aria-hidden="true"><circle cx="120" cy="120" r="120" fill="var(--grey)"/></svg>
  <div class="legal">St.-Nr. 12 345 678, Beispielbank Nord, BLZ 200 300 40<br>IBAN DE00 2003 0040 0012 3456 78, BIC BEISDEHH<br>USt-IdNr. DE123456789</div>
</section>

<section class="card-small" aria-label="Visitenkarte">
  <div class="brand">Lena Marwitz</div>
  <div class="services">Textredaktion<br>Korrektorat<br>Ghostwriting</div>
  <svg class="deco" width="50" height="50" aria-hidden="true"><circle cx="25" cy="25" r="25" fill="var(--grey)"/></svg>
  <div class="name">Lena <b>Marwitz</b></div>
  <div class="contact">Lindenhofweg 7<br>24103 Kiel<br>Tel: (0 431) 7 62 40 19<br>l.marwitz@post-beispiel.de</div>
</section>

<section class="brand-block" aria-label="Logo und Absender">
  <div class="brand">Lena Marwitz</div>
  <div class="services-line">Korrektorat • Textredaktion • Ghostwriting</div>
  <div class="sender">Lena <b>Marwitz</b><div class="services">Korrektorat<br>Textredaktion<br>Ghostwriting</div></div>
  <div class="contact">Lindenhofweg 7<br>24103 Kiel<br>Tel. (0 431) 7 62 40 18<br>l.marwitz@post-beispiel.de</div>
</section>

<section class="card-large" aria-label="Visitenkarte groß">
  <div class="brand">Lena Marwitz</div>
  <div class="services">Textredaktion<br>Korrektorat<br>Ghostwriting</div>
  <svg class="deco" width="130" height="130" aria-hidden="true"><circle cx="65" cy="65" r="65" fill="var(--grey)"/></svg>
  <div class="name">Lena <b>Marwitz</b></div>
  <div class="contact">Lindenhofweg 7<br>24103 Kiel<br>Tel: (0 431) 7 62 40 19<br>l.marwitz@post-beispiel.de</div>
</section>

<div class="palette-label">lena.marwitz.projekt</div>
<div class="palette" aria-label="Farbpalette">
  <div class="swatch black"></div>
  <div class="swatch blue"></div>
  <div class="swatch light-blue"></div>
</div>

</body>
</html>
```